Harbourline Electrical limited business card design

I need a business card made up it must be double sided with just my logo and some graphic one side and then on the reverse a little description of services I provide along with my email address phone number and face book and instagram handles
I already had a logo designed by pixel meadow and the social media pack so I’m thinking to use the social media design as the main image
Services I provide are: domestic commercial industrial sub contract from bathroom's and kitchen’s to outside lights and sockets no job to big or to small

Industry/Entity Type

Electrician/construction industry

Contact Information for Business Card

Email address: harbourlineelectrical@mailvane.com mobile number: 07855402917 fb: Harbourline Electrical insta: @harbourlineelectrical

Font styles to use
Sans Serif

Colors
0094D4
00A9DD
6FCCEA
C7EBF8
E9F6FB
FFF300
FFF600
FEFA6F
FFFEC7
FFFEE8

Requirements
Must have
• Double sided, fb and insta handles contact info, domestic commercial industrial sub contract
Nice to have
• From bathroom's and kitchen’s to outside outside lights and sockets no job to big or to small

```html
<!DOCTYPE html>
<html lang="en">
<head>
<meta charset="utf-8">
<title>Harbourline Electrical – Business Card</title>
<link href="https://fonts.googleapis.com/css2?family=Montserrat:wght@800&family=Roboto:wght@400;500;700&display=swap" rel="stylesheet">
<style>
  :root {
    --backdrop: #5e5f61;
    --card-light: #ffffff;
    --card-edge: #dcdde0;
    --brand-blue: #1a86c8;
    --brand-blue-deep: #0f74b8;
    --accent-gold: #eeb02f;
    --accent-gold-soft: rgba(238, 176, 47, 0.55);
    --accent-blue-soft: rgba(26, 134, 200, 0.35);
    --ink: #222222;
  }
  * { margin: 0; padding: 0; box-sizing: border-box; }
  html, body { width: 900px; height: 1200px; overflow: hidden; }
  body { background: var(--backdrop); position: relative; font-family: "Roboto", sans-serif; }

  .card {
    position: absolute;
    left: 150px;
    width: 600px;
    height: 386px;
    overflow: hidden;
    background: radial-gradient(ellipse at 50% 45%, var(--card-light) 0%, #f1f1f2 45%, var(--card-edge) 100%);
  }
  .card--front { top: 200px; }
  .card--back { top: 614px; }

  .corner-art {
    position: absolute;
    width: 230px;
    height: 200px;
  }
  .corner-art--top-left {
    left: 0; top: 0;
    background: linear-gradient(135deg, var(--accent-blue-soft) 0%, var(--accent-gold-soft) 35%, rgba(238, 176, 47, 0) 75%);
  }
  .corner-art--bottom-right {
    right: 0; bottom: 0;
    background: linear-gradient(315deg, var(--accent-blue-soft) 0%, var(--accent-gold-soft) 35%, rgba(238, 176, 47, 0) 75%);
  }

  .brand {
    position: absolute;
    left: 0; right: 0;
    top: 120px;
    display: flex;
    flex-direction: column;
    align-items: center;
  }
  .brand__circle {
    width: 100px; height: 100px;
    border-radius: 50%;
    border: 4px solid var(--brand-blue);
  }
  .brand__name {
    margin-top: 20px;
    font-family: "Montserrat", sans-serif;
    font-weight: 800;
    color: var(--brand-blue);
    font-size: 30px;
    line-height: 1;
    letter-spacing: 0.5px;
    text-transform: uppercase;
  }
  .brand__sub {
    margin-top: 8px;
    font-family: "Montserrat", sans-serif;
    font-weight: 800;
    color: var(--brand-blue);
    font-size: 13px;
    letter-spacing: 13px;
    text-transform: uppercase;
    padding-left: 13px;
  }

  .contact-block { position: absolute; left: 44px; top: 110px; }
  .contact-block__name {
    font-weight: 700;
    font-size: 24px;
    color: var(--brand-blue-deep);
    line-height: 1;
  }
  .contact-block__role {
    margin-top: 8px;
    font-size: 14.5px;
    color: var(--ink);
    letter-spacing: 0.6px;
  }
  .contact-list { list-style: none; margin-top: 12px; }
  .contact-list__item {
    display: flex; align-items: center;
    font-size: 15px;
    color: var(--ink);
    letter-spacing: 0.7px;
    height: 22.5px;
  }
  .contact-list__icon { width: 12px; height: 12px; margin-right: 4px; flex: none; }

  .emblem {
    position: absolute;
    left: 361px; top: 121px;
    width: 166px; height: 166px;
    border-radius: 50%;
    border: 5px solid var(--brand-blue);
  }

  .services {
    position: absolute;
    top: 333px;
    left: 0;
    width: 600px;
    height: 24px;
    font-weight: 700;
    font-size: 17.5px;
    color: var(--brand-blue);
  }
  .services__item { position: absolute; top: 0; line-height: 24px; }
  .services__divider {
    position: absolute;
    top: 3px;
    width: 2px;
    height: 18px;
    background: var(--accent-gold);
  }
</style>
</head>
<body>

<section class="card card--front" aria-label="Business card front">
  <div class="corner-art corner-art--top-left" role="img" aria-label="Corner graphic of a lightning bolt over a patterned border"></div>
  <div class="corner-art corner-art--bottom-right" role="img" aria-label="Corner graphic of a lightning bolt over a patterned border"></div>

  <div class="brand">
    <div class="brand__circle" role="img" aria-label="Company emblem"></div>
    <div class="brand__name">Harbourline</div>
    <div class="brand__sub">Electrical</div>
  </div>
</section>

<section class="card card--back" aria-label="Business card back">
  <div class="contact-block">
    <h1 class="contact-block__name">Tobias Renner</h1>
    <p class="contact-block__role">Owner</p>
    <ul class="contact-list">
      <li class="contact-list__item">
        <svg class="contact-list__icon" viewBox="0 0 12 12"><path d="M2.4,0.6 L4.2,2.8 L3.3,4.1 Q4.3,6.6 7.8,8.7 L9,7.7 L11.4,9.4 L10.3,11.4 Q5.6,11.4 2.4,7.5 Q0.3,4.6 0.8,1.6 Z" fill="var(--brand-blue)"/></svg>
        07855402917
      </li>
      <li class="contact-list__item">
        <svg class="contact-list__icon" viewBox="0 0 12 12"><rect x="0.5" y="2.5" width="11" height="7.5" fill="var(--brand-blue)"/><path d="M0.8,2.8 L6,7 L11.2,2.8" fill="none" stroke="#fff" stroke-width="1"/></svg>
        harbourlineelectrical@mailvane.com
      </li>
      <li class="contact-list__item">
        <svg class="contact-list__icon" viewBox="0 0 12 12"><circle cx="6" cy="6" r="5.5" fill="var(--brand-blue)"/></svg>
        Harbourline Electrical
      </li>
      <li class="contact-list__item">
        <svg class="contact-list__icon" viewBox="0 0 12 12"><circle cx="6" cy="6" r="5.5" fill="var(--brand-blue)"/></svg>
        @harbourlineelectrical
      </li>
    </ul>
  </div>

  <div class="emblem" role="img" aria-label="Company emblem"></div>

  <div class="services">
    <span class="services__item" style="left:43px">DOMESTIC</span>
    <span class="services__divider" style="left:144px"></span>
    <span class="services__item" style="left:157px">COMMERCIAL</span>
    <span class="services__divider" style="left:284px"></span>
    <span class="services__item" style="left:297px">INDUSTRIAL</span>
    <span class="services__divider" style="left:411px"></span>
    <span class="services__item" style="left:424px">SUB CONTRACT</span>
  </div>
</section>

</body>
</html>
```